Thriving Mexican import business needs a new business card

Need a refresher of our current business card. Looking for a lighter background with the logo on one side. We will want this file to be adjustable so we can change names, emails and mobile numbers.
We are open to ideas but maintaining a professional image is critical.
Thankyou,

Target Market(s)

Anyone in food industry

Industry/Entity Type

Wholesale

Contact Information for Business Card

Mark Pendlebury
Director
Condor Provisions & Spirits Pty Ltd
5B Morrow Ct, Kelvinbrook VIC 3127
0421930576 (03) 95128460
mark@condorlatino.example.au
condorlatinoprovisionsandspirits.example.au

Font styles to use
Serif
Other font styles liked:
• NeoGram Heavy

Requirements
Must have
• Professional yet memorable
Condor logo
Nice to have
• Chilli or tequila/mexican food pictures
Should not have
• Dark background

```html
<!DOCTYPE html>
<html lang="en">
<head>
<meta charset="utf-8">
<title>Condor Provisions &amp; Spirits – Business Card</title>
<link href="https://fonts.googleapis.com/css2?family=Lato:wght@400;700;900&display=swap" rel="stylesheet">
<style>
  :root {
    --stage: #dcd9d4;
    --card: #f8f6f2;
    --ink: #161616;
    --muted: #5e5e5e;
    --rule: #2a2a2a;
  }
  * { box-sizing: border-box; margin: 0; padding: 0; }
  html, body { width: 1200px; height: 847px; overflow: hidden; }
  body {
    background: var(--stage);
    font-family: "Lato", sans-serif;
    display: flex;
    align-items: center;
    justify-content: center;
    gap: 48px;
  }
  .card {
    position: relative;
    width: 540px;
    height: 310px;
    background: var(--card);
    color: var(--ink);
    box-shadow: 0 10px 28px rgba(0,0,0,.18);
  }
  .brand {
    display: flex;
    align-items: center;
    gap: 10px;
    font-weight: 900;
    text-transform: uppercase;
    color: var(--ink);
    line-height: 1;
  }
  .brand-mark { background: var(--ink); display: block; }

  /* front */
  .card-front .brand {
    position: absolute;
    left: 50%; top: 50%;
    transform: translate(-50%, -50%);
    font-size: 46px;
    letter-spacing: 1px;
  }
  .card-front .brand-mark { width: 30px; height: 30px; }

  /* back */
  .person { position: absolute; left: 30px; top: 42px; }
  .person-name { font-weight: 700; font-size: 19px; }
  .person-role { font-size: 10px; color: var(--muted); margin-top: 3px; }

  .card-back .brand {
    position: absolute;
    right: 32px; top: 72px;
    font-size: 36px;
    letter-spacing: 1px;
  }
  .card-back .brand-mark { width: 24px; height: 24px; }

  .divider {
    position: absolute;
    left: 30px; right: 30px; top: 128px;
    border-top: 1px solid var(--rule);
  }

  .contacts {
    position: absolute;
    left: 30px; top: 142px;
    list-style: none;
    font-size: 11px;
    color: var(--muted);
  }
  .contacts li { display: flex; align-items: center; gap: 8px; height: 17px; }
  .contacts svg { width: 10px; height: 10px; fill: var(--muted); stroke: var(--muted); flex: none; }
  .contacts .icon-line { fill: none; stroke-width: 0.9; }

  .company {
    position: absolute;
    right: 32px; bottom: 34px;
    text-align: right;
  }
  .company-name { font-weight: 700; font-size: 11.5px; }
  .company-address { font-size: 11px; color: var(--muted); margin-top: 4px; }
</style>
</head>
<body>
  <section class="card card-front" aria-label="Card front">
    <div class="brand"><span class="brand-mark"></span>Condor</div>
  </section>

  <section class="card card-back" aria-label="Card back">
    <div class="person">
      <div class="person-name">Mark Pendlebury</div>
      <div class="person-role">Director</div>
    </div>

    <div class="brand"><span class="brand-mark"></span>Condor</div>

    <div class="divider"></div>

    <ul class="contacts">
      <li><svg viewBox="0 0 10 10" aria-hidden="true"><path stroke="none" d="M2 0.5 L3.6 0.5 L4.3 2.6 L3.2 3.5 Q4.2 5.8 6.5 6.8 L7.4 5.7 L9.5 6.4 L9.5 8 Q9.5 9.5 8 9.5 Q1 9 0.5 2 Q0.5 0.5 2 0.5 Z"/></svg>0421 930 576</li>
      <li><svg viewBox="0 0 10 10" aria-hidden="true"><path stroke="none" d="M2 0.5 L3.6 0.5 L4.3 2.6 L3.2 3.5 Q4.2 5.8 6.5 6.8 L7.4 5.7 L9.5 6.4 L9.5 8 Q9.5 9.5 8 9.5 Q1 9 0.5 2 Q0.5 0.5 2 0.5 Z"/></svg>(03) 9512 8460</li>
      <li><svg viewBox="0 0 10 10" aria-hidden="true"><path class="icon-line" d="M0.5 1.8 H9.5 V8.2 H0.5 Z M0.8 2.2 L5 5.5 L9.2 2.2"/></svg>mark@condorlatino.example.au</li>
      <li><svg viewBox="0 0 10 10" aria-hidden="true"><circle class="icon-line" cx="5" cy="5" r="4.4"/><path class="icon-line" d="M0.6 5 H9.4 M5 0.6 V9.4"/></svg>condorlatinoprovisionsandspirits.example.au</li>
    </ul>

    <div class="company">
      <div class="company-name">Condor Provisions &amp; Spirits Pty Ltd</div>
      <div class="company-address">5B Morrow Ct, Kelvinbrook VIC 3127</div>
    </div>
  </section>
</body>
</html>
```